The Fern Lantern Pub- restaurant menu, new launch

This is a new restaurant launching Summer 2017. Restaurant is a conversion of long standing small town existing family pizza/italian restaurant. new concept shifts concept to a family pub atmosphere featuring familiar appetizers, burgers, wood-fired pizza, and daily specials, draft beer, full- bar.

atmosphere is casual. want menu to reflect a more current "vibe" than the old place did. Not cold and modern, but retain the cozy familiar feel, without seeming dated and old fashioned.

4 panel menu; 8.5 X 11; 2-4 color
Updates

Project Deadline Extended
Reason: I am interested in seeing more designs. I will be providing feedback in the next few days on all designs submitted. I will also be increasing the budget.

Target Market(s)

Family-Oriented Pub, rural location Berkshire County, MA. Mostly Blue collar customer, value oriented

Industry/Entity Type

American Restaurant

Font styles to use
Sans Serif

Colors

Designer to choose colors to be used in the design.

Requirements
Must have
• Clear, uncluttered design, Highlighted items as specified in draft file (to come)
• ability to make changes daily as menu changes
• each panel separate sheet to slide into binder sleeve

```html
<!DOCTYPE html>
<html lang="en">
<head>
<meta charset="utf-8">
<title>The Fern Lantern Pub – Menu</title>
<link href="https://fonts.googleapis.com/css2?family=Cabin+Sketch:wght@700&family=Gochi+Hand&family=Amatic+SC:wght@700&display=swap" rel="stylesheet">
<style>
:root{
  --board:#262626;
  --board-edge:#1b1b1b;
  --chalk:#e6e6e6;
  --title:#c7cdd1;
  --teal:#7fc9cb;
  --purple:#9a82d6;
  --tan:#e3a26a;
  --green:#62c23c;
  --lime:#a8d45a;
  --red:#d2482f;
  --gold:#dca83c;
  --olive:#c9c257;
  --pink:#cf4d92;
  --blue:#7392dc;
  --mauve:#b58bc8;
  --icon:#5a5a5a;
}
*{margin:0;padding:0;box-sizing:border-box}
html,body{width:925px;height:1200px;overflow:hidden;background:var(--board-edge)}
.menu{position:relative;width:925px;height:1200px}
.panel{position:absolute;width:462px;height:600px;overflow:hidden;
  background:radial-gradient(ellipse at 50% 40%,#333 0%,var(--board) 60%,var(--board-edge) 100%);
  color:var(--chalk);font-family:"Gochi Hand",cursive}
.p1{left:0;top:0}.p2{left:463px;top:0}.p3{left:0;top:600px}.p4{left:463px;top:600px}
.pub-name{position:absolute;left:0;right:0;top:10px;text-align:center;font-family:"Cabin Sketch",sans-serif;font-weight:700;font-size:31px;line-height:31px;color:var(--title);letter-spacing:1px}
.head{position:absolute;font-family:"Cabin Sketch",sans-serif;font-weight:700;font-size:24px;line-height:26px;letter-spacing:.5px;white-space:nowrap}
.head.sm{font-size:18px;line-height:22px}
.center{left:0;right:0;text-align:center}
.spaced{letter-spacing:5px}
.price{position:absolute;font-family:"Amatic SC",sans-serif;font-weight:700;font-size:25px;line-height:26px;color:var(--chalk);white-space:nowrap}
.price.tiny{font-size:11px;line-height:11px}
.desc{position:absolute;font-size:10px;line-height:11px;color:var(--chalk)}
.list{position:absolute;font-size:10px;line-height:11px}
.icon{position:absolute;background:var(--icon);border-radius:8px;opacity:.7}
.c-teal{color:var(--teal)}.c-purple{color:var(--purple)}.c-tan{color:var(--tan)}.c-green{color:var(--green)}
.c-lime{color:var(--lime)}.c-red{color:var(--red)}.c-gold{color:var(--gold)}.c-olive{color:var(--olive)}
.c-pink{color:var(--pink)}.c-blue{color:var(--blue)}.c-mauve{color:var(--mauve)}
</style>
</head>
<body>
<div class="menu">

<!-- Panel 1: starters, soups, salads -->
<section class="panel p1">
  <div class="pub-name">THE FERN<br>LANTERN PUB</div>

  <div class="head c-teal" style="left:10px;top:90px">WINGS</div>
  <div class="price" style="left:394px;top:90px">12,00 $</div>
  <div class="desc" style="left:24px;top:118px;width:340px">A Baker's Ten (that's 11) of the biggest tastiest wings you'll find anywhere. Choose from our award winning sauces:</div>
  <div class="list" style="left:40px;top:141px">Buffalo mild<br>Buffalo hot<br>Maple's Honey Chipotle<br>Garlic Parm<br>BBQ<br>Xtra Hot<br>Challenge Hot</div>

  <div class="head c-purple" style="left:10px;top:220px">BONELESS "WINGS"</div>
  <div class="price" style="left:394px;top:222px">12,00 $</div>
  <div class="desc" style="left:24px;top:248px;width:360px">Why are they called wings? They're not wings. But it's tasty boneless breaded chicken anyway. Same great sauces, 8 "Wings."</div>

  <div class="head c-tan" style="left:10px;top:275px">'CHOS!!</div>
  <div class="price" style="left:394px;top:278px">11,00 $</div>
  <div class="desc" style="left:24px;top:304px">Totchos and Nachos and Cheese, oh my!</div>
  <div class="list" style="left:40px;top:318px">Add brisket<br>Add pulled pork<br>Add chili</div>
  <div class="price tiny" style="left:394px;top:319px">3,00 $<br>3,00 $<br>3,00 $</div>
  <div class="icon" role="img" aria-label="Chalk drawing of a nacho bowl" style="left:252px;top:294px;width:50px;height:44px;border-radius:0 0 25px 25px"></div>

  <div class="head c-green" style="left:10px;top:352px">SPINACH ARTICHOKE DIP</div>
  <div class="price" style="left:394px;top:355px">10,00 $</div>
  <div class="desc" style="left:24px;top:382px;width:340px">The good stuff. Real Spinach. Real Artichokes. Real Cheese. This did not come from a bag. We make it right here, every day.</div>

  <div class="head sm c-red spaced" style="left:118px;top:410px">SOUPS &amp; STUFF</div>
  <div class="head sm c-purple" style="left:10px;top:434px">CHOWDER<br>CHILI<br>DU JOUR</div>
  <div class="price" style="left:412px;top:434px;line-height:22px">6,00 $<br>6,00 $<br>6,00 $</div>
  <div class="icon" role="img" aria-label="Chalk drawing of a soup bowl" style="left:126px;top:450px;width:50px;height:44px;border-radius:4px 4px 25px 25px"></div>

  <div class="head sm c-teal spaced" style="left:176px;top:502px">SALADS</div>
  <div class="head sm c-green" style="left:10px;top:526px">FERN LANTERN CHOPPED SALAD<br>GORGONZOLA SALAD</div>
  <div class="price" style="left:394px;top:526px;line-height:22px">12,00 $<br>12,00 $</div>
  <div class="icon" role="img" aria-label="Chalk drawing of a salad bowl" style="left:326px;top:528px;width:44px;height:30px;border-radius:4px 4px 22px 22px"></div>
  <div class="desc" style="left:24px;top:572px">Add chicken</div>
  <div class="price tiny" style="left:394px;top:574px">2,00 $</div>
</section>

<!-- Panel 2: wood fired pizza -->
<section class="panel p2">
  <div class="pub-name">THE FERN<br>LANTERN PUB</div>

  <div class="head c-gold center" style="top:88px">WOOD FIRED PIZZA</div>
  <div class="icon" role="img" aria-label="Chalk drawing of a pizza" style="left:16px;top:114px;width:38px;height:38px;border-radius:50%"></div>
  <div class="desc" style="left:60px;top:118px;width:380px;text-align:center">All our dough is made fresh daily in house with just four ingredients: water flour salt and yeast. Baked to perfection in the wood oven, Fern Lantern Pizza is the best in the county!</div>

  <div class="head c-pink center" style="top:154px">OUR SPECIALITY PIES</div>
  <div class="head c-pink" style="left:8px;top:182px;font-size:27px;line-height:30px">SMALL<br>LARGE</div>
  <div class="price" style="left:392px;top:185px;line-height:28px">13,00 $<br>17,00 $</div>
  <div class="icon" role="img" aria-label="Chalk drawing of a small pie" style="left:104px;top:184px;width:48px;height:22px;border-radius:50% 50% 10px 10px"></div>
  <div class="icon" role="img" aria-label="Chalk drawing of a large pie" style="left:136px;top:196px;width:84px;height:36px;border-radius:50% 50% 12px 12px"></div>
  <div class="desc" style="left:30px;top:242px;width:400px;text-align:center">The Buffalo Bird buffalo sauce, grilled chicken, mozzarella and topped with red onion for just the right finish. Don't like onion? We'll leave it off!</div>
  <div class="desc" style="left:20px;top:274px;width:420px;text-align:center">Chicken 'Q' - house made BBQ<br>sauce from Oak Ridge BBQ, Grilled chicken and mozzarella make this crowd favorite.</div>
  <div class="desc" style="left:30px;top:306px;width:400px;text-align:center">The Hula Hula - Sliced ham and Pineapple, and mozzarella.<br>It doesn't get any better! Ask for coconut, if you're feeling crazy!</div>

  <div class="head c-red center" style="top:332px">CREATE YOUR OWN!</div>
  <div class="head c-red" style="left:8px;top:362px;font-size:27px;line-height:30px">SMALL<br>LARGE</div>
  <div class="price" style="left:392px;top:365px;line-height:28px">11,00 $<br>10,00 $</div>
  <div class="desc" style="left:24px;top:422px">Choose from standard toppings:</div>
  <div class="desc" style="left:36px;top:436px;width:340px">Pepperoni, Onion, Tomato, Garlic, Green Pepper, Mushroom, Sliced or Chopped Tomato, Broccoli, Spinach, Sliced black olives</div>
  <div class="desc" style="left:24px;top:458px">More meats:</div>
  <div class="desc" style="left:36px;top:472px">Meatball, Bacon, Sausage, Chicken, Ham</div>
  <div class="desc" style="left:18px;top:489px">Speciality toppings:</div>
  <div class="desc" style="left:36px;top:503px;width:360px">Xtra Cheese, Pineapple, Feta, Ricotta, Kalamata Olives, Hot Peppers, Coconut, Artichokes, Sun dried Tomato, Pesto</div>
  <div class="desc" style="left:24px;top:528px">Gluten Free add<br>(only small size)</div>
  <div class="price tiny" style="left:400px;top:424px">2,00 $</div>
  <div class="price tiny" style="left:400px;top:460px">2,50 $</div>
  <div class="price tiny" style="left:400px;top:490px">3,00 $</div>
  <div class="price tiny" style="left:400px;top:530px">2,00 $</div>

  <div class="head sm c-teal center" style="top:553px">FOLD IT UP!</div>
  <div class="desc center" style="top:580px">Turn your Pizza into a calzone, specialty or build your own. Same price as a small.</div>
</section>

<!-- Panel 3: burgers -->
<section class="panel p3">
  <div class="pub-name">THE FERN<br>LANTERN PUB</div>

  <div class="icon" role="img" aria-label="Chalk drawing of a burger" style="left:20px;top:82px;width:64px;height:58px;border-radius:30px 30px 10px 10px"></div>
  <div class="head c-olive" style="left:138px;top:114px;font-size:27px">FERN BURGERS</div>
  <div class="desc" style="left:24px;top:148px;width:340px">Our ground beef is pure 80/20 goodness, from Ridgeline Farms, always fresh, hand packed daily for exceptional beef burger taste. Accept no substitutes - these are the best burgers anywhere.</div>

  <div class="head c-tan" style="left:10px;top:190px">THE FERN BURGER 'ORIGINAL'</div>
  <div class="price" style="left:394px;top:192px">10,99 $</div>
  <div class="desc" style="left:24px;top:222px;width:350px">Double 1/4 lb hand packed patties, with double American cheese, and double the Green Hollow Smokehouse Applewood Bacon. This beauty is served with Lettuce, Tomato, Onion, our world-class hand-cut fries, and a side of Fern Sauce.</div>

  <div class="head c-blue center" style="top:280px;line-height:22px">WANT TO DO IT YOUR WAY?<br>OVER 100 POSSIBILITIES!</div>
  <div class="list c-pink" style="left:24px;top:334px;line-height:10.5px">¼ lb patty<br>Double ¼<br>Triple ¼<br>Quad quarter</div>
  <div class="price tiny" style="left:394px;top:334px;line-height:10.5px">6,00 $<br>8,00 $<br>9,00 $<br>10,00 $</div>
  <div class="list c-pink" style="left:24px;top:382px;line-height:10.5px">1/3 lb patty<br>Double 1/3<br>Triple 1/3<br>Quad 1/3</div>
  <div class="price tiny" style="left:394px;top:382px;line-height:10.5px">8,00 $<br>11,00 $<br>13,00 $<br>15,00 $</div>
  <div class="icon" role="img" aria-label="Chalk drawing of an open burger bun" style="left:256px;top:408px;width:86px;height:48px;border-radius:24px"></div>

  <div class="head sm c-green" style="left:10px;top:428px">ADD-ONS</div>
  <div class="list c-teal" style="left:24px;top:456px">Lettuce, Tomato, Onion, Pickle - no charge<br>Sliced Cheese - American, Cheddar, Swiss<br>Gorgonzola</div>
  <div class="list c-teal" style="left:24px;top:492px;line-height:13px">Green Hollow Smokehouse Applewood Bacon<br>World-Class Hand-cut Fries</div>
  <div class="price tiny" style="left:394px;top:458px;line-height:13px">0,75 $<br>1,00 $<br>1,00 $<br>2,50 $</div>
  <div class="icon" role="img" aria-label="Chalk drawing of a bread roll" style="left:256px;top:520px;width:90px;height:56px;border-radius:28px"></div>
</section>

<!-- Panel 4: daily specials -->
<section class="panel p4">
  <div class="pub-name">THE FERN<br>LANTERN PUB</div>

  <div class="head c-lime center" style="top:100px;font-size:26px">DAILY SPECIAL</div>
  <div class="head sm c-green center" style="top:126px;font-size:15px">WHERE THE CRAZINESSS HAPPENS</div>

  <div class="head sm c-tan" style="left:8px;top:168px">20 LAYER LASAGNA</div>
  <div class="icon" role="img" aria-label="Chalk drawing of a lasagna slice" style="left:228px;top:156px;width:52px;height:32px;border-radius:4px"></div>
  <div class="price" style="left:392px;top:168px">12,99 $</div>
  <div class="desc" style="left:24px;top:197px">Our signature dish sells out every week, get it when you can!</div>

  <div class="head sm c-mauve" style="left:8px;top:218px">THE PIG PILE</div>
  <div class="icon" role="img" aria-label="Chalk drawing of a pig" style="left:195px;top:214px;width:32px;height:28px;border-radius:50%"></div>
  <div class="price" style="left:392px;top:218px">11,00 $</div>
  <div class="desc" style="left:24px;top:245px;width:340px">Our World-class Hand-cut fries topped with Pulled pork, Mozzarella, Crispy Bacon, BBQ sauce, and Topped with house onion rings. Not for the faint of heart, if you know what we mean...</div>

  <div class="head sm c-green" style="left:8px;top:288px">PASTA PRIMAVERA</div>
  <div class="icon" role="img" aria-label="Chalk drawing of a pasta plate" style="left:334px;top:278px;width:44px;height:44px;border-radius:50%"></div>
  <div class="price" style="left:392px;top:288px">12,99 $</div>
  <div class="desc" style="left:24px;top:316px">Fresh veggies, tossed with penne, in a garlic white wine butter sauce.</div>

  <div class="head sm c-tan" style="left:8px;top:336px">CHICKEN PARMESAN</div>
  <div class="icon" role="img" aria-label="Chalk drawing of a roast chicken" style="left:258px;top:334px;width:46px;height:26px;border-radius:50%"></div>
  <div class="price" style="left:392px;top:336px">15,00 $</div>
  <div class="desc" style="left:24px;top:362px;width:340px">Two breaded chicken breasts topped with house marinara and mozzarella, served with penne marinara. Yum.</div>

  <div class="head sm c-red" style="left:8px;top:388px">PASTA CARBONARA</div>
  <div class="icon" role="img" aria-label="Chalk drawing of a spaghetti plate" style="left:264px;top:382px;width:44px;height:34px;border-radius:50%"></div>
  <div class="price" style="left:392px;top:388px">15,00 $</div>
  <div class="desc" style="left:24px;top:416px">The creamy bacon pasta classic. You know it, you love it. Just say yes.</div>

  <div class="head sm c-red" style="left:8px;top:440px">BUFFALO CHICKEN MAC AND CHEESE</div>
  <div class="price" style="left:392px;top:438px">13,00 $</div>
  <div class="desc" style="left:24px;top:466px">All the food groups in this one!<br>Chicken, Buffalo sauce, Mac and Cheese. A true food pyramid!</div>
  <div class="icon" role="img" aria-label="Chalk drawing of cheese and a buffalo" style="left:278px;top:534px;width:86px;height:46px"></div>
</section>

</div>
</body>
</html>
```